Design for iOS app - Scanner App

We are developing an iOS app that is scanning receipts and mailing them to a predefined email address. The app should work more or less like TallySnap app (a short demo of the TallySnap app is available here: https://www.clipvault.example/watch?v=QmRtZpLwXkA).

We have prototyped the app in the link below:
http://app.wirepane.example/view/a71c3d9f2b8e40c6d5f18e27b9a4c3d0

NB!: Please do not follow the mockups literally, but the iOS Human Interface Guidelines!

The technical specifications and descriptions of the app's functionalities are available in the link below:
https://sheets.papyrdesk.example/document/d/9pQrx-TW2cNmbvJLhQ7dKzR4eWs-aY_3Hkv8Tfmn5xe/edit?usp=sharing

Requirements for the design:

- The design should be provided as PSD, where each page/section should be in its own PSD file OR all pages/sections should be represented as folder groups in a single PSD file.

- All graphical elements in the design should be delivered as single layers which can then be extracted from the PSD.

- All graphical elements (icons, graphical buttons, etc.) should be provided as vector objects in the PSD, so that they can be exported into different sizes without loss of quality (for responsiveness).

- The design should use either web safe fonts or Quorby Fonts.

Instructions for the design:

The design should have habitual user interface like ordinary iOS navigation stack, with navigation bar on the top and all other elements on the bottom. That means just to make the top bar in your app be more like iOS. Please follow the iOS Human Interface Guidelines, not the mockups literally .
FX: the e small elements in Dimensions screen like delete icons and active checkbox. In
https://devhub.orchardly.example/library/ios/documentation/UserExperience/Conceptual/MobileHIG/LayoutandAppearance.html#//ref/doc/uid/TP51208847-CH31-SW1
is described that interface elements should be at least 44x44 px - it's normal practice for all mobile development (iOS, android), so you should consider this too.

Please also provide an app icon and suggest a logo for the app.

Requirements
Must have
• Please make sure that the design is flat. Like iOS app, Pagefold, Quorby apps etc.
Nice to have
• The design could be somewhat like the design for Mindvale Pagefold(https://apps.orchardly.example/bg/app/mindvale-pagefold/id552719043?mt=8) without being too similar
Should not have
• 3D look

```html
<!DOCTYPE html>
<html lang="en">
<head>
<meta charset="utf-8">
<title>SLIPT – Presentation Apps</title>
<link rel="stylesheet" href="https://fonts.googleapis.com/css2?family=Ubuntu:wght@400;500;700&display=swap">
<style>
:root{
  --red:#e5493a;
  --red-dark:#c93a2d;
  --teal:#27b59b;
  --blue:#3cb3e6;
  --ink:#3a3a3a;
  --muted:#8d8d8d;
  --line:#dcdcdc;
  --panel:#f3f3f3;
  --field:#e6e6e6;
  --stage-top:#3b3b3b;
  --stage-bottom:#262626;
  --white:#ffffff;
}
*{box-sizing:border-box;margin:0;padding:0}
html,body{width:1200px;height:3165px;overflow:hidden}
body{font-family:"Ubuntu",sans-serif;color:var(--ink);background:linear-gradient(var(--stage-top),var(--stage-bottom));position:relative}

/* ---------- header ---------- */
.masthead{position:absolute;left:0;top:0;width:1200px;height:119px;background:var(--red);display:flex;align-items:center;justify-content:space-between;padding:0 52px}
.brand{display:flex;align-items:center;gap:18px;color:var(--white);font-weight:700;font-size:58px;letter-spacing:-1px}
.brand-mark{width:56px;height:56px;border:5px solid var(--white);border-radius:6px}
.masthead-title{color:var(--white);font-size:34px;font-weight:500;letter-spacing:1px}

/* ---------- hero ---------- */
.hero{position:absolute;top:119px;left:0;width:1200px;height:540px;display:flex}
.hero-shot{flex:1;position:relative}
.hero-shot.home{background:linear-gradient(135deg,#9aa3ab,#d9dde0 45%,#7d8892)}
.hero-shot.hand{background:linear-gradient(120deg,#3d3d3d,#6a6a6a 50%,#b8bcc0);border-left:4px solid #1f1f1f}
.hero-callout{position:absolute;left:34px;bottom:30px;color:var(--white);font-size:22px;line-height:1.2;letter-spacing:2px}
.hero-callout::after{content:"";position:absolute;left:112px;top:12px;width:130px;height:2px;background:var(--white)}

/* ---------- board ---------- */
.board{position:absolute;left:75px;top:807px;display:grid;grid-template-columns:repeat(4,236px);column-gap:30px;grid-auto-rows:606px}
.cell{display:flex;flex-direction:column;align-items:center}
.caption{margin-top:56px;color:#e6e6e6;font-size:22px}

/* ---------- screen ---------- */
.screen{width:236px;height:420px;background:var(--panel);position:relative;overflow:hidden;display:flex;flex-direction:column;font-size:10px;box-shadow:0 0 0 3px #1c1c1c}
.status{height:10px;background:var(--red-dark);flex:none}
.nav{height:34px;background:var(--red);flex:none;display:flex;align-items:center;justify-content:space-between;padding:0 9px}
.nav-name{color:var(--white);font-weight:700;font-size:17px;letter-spacing:-.3px}
.nav-icons{display:flex;gap:6px;width:32px;justify-content:flex-end}
.nav-side{width:32px;display:flex}
.section-head{background:var(--field);padding:7px 9px;font-weight:500;font-size:10px;display:flex;align-items:center;gap:5px}
.body{flex:1;position:relative;display:flex;flex-direction:column}
.stack{display:flex;flex-direction:column;gap:5px;padding:0 9px 10px;margin-top:auto}
.btn{height:28px;display:flex;align-items:center;justify-content:center;color:var(--white);font-size:10px}
.btn.teal{background:var(--teal)}
.btn.blue{background:var(--blue)}
.btn.red{background:var(--red)}

/* main */
.scan-button{width:112px;height:112px;border-radius:50%;background:var(--red);box-shadow:0 0 0 6px var(--white),0 0 0 8px #e8c4c0;margin:48px auto 0;display:flex;align-items:center;justify-content:center;text-align:center;color:var(--white);font-weight:700;font-size:13px;line-height:1.15}
.scan-state{text-align:center;color:var(--muted);font-size:8px;margin-top:30px;letter-spacing:1px}
.counter{display:flex;height:26px;margin:0 9px 5px;color:var(--white);font-size:10px}
.counter .name{flex:1;display:flex;align-items:center;padding-left:8px}
.counter .num{width:34px;display:flex;align-items:center;justify-content:center}
.counter.pending .name{background:var(--blue)} .counter.pending .num{background:#2a8fbd}
.counter.sent .name{background:var(--teal)} .counter.sent .num{background:#1d8f7a}
.counters{margin-top:auto;padding-bottom:8px}

/* dialog screens */
.notice{padding:0 18px;text-align:center;font-size:9px;line-height:1.4;margin-top:54px;position:relative}
.notice strong{font-weight:700}
.notice .hl{color:var(--red)}
.ring{position:absolute;left:50%;top:-16px;width:100px;height:100px;margin-left:-50px;border-radius:50%;border:14px solid rgba(229,73,58,.08);z-index:-1}
.notice{z-index:0}
.ghost{opacity:.18;margin-top:auto;padding-bottom:8px}

/* forms */
.field-label{padding:8px 9px 3px;font-size:9px}
.field{height:20px;background:var(--field);margin:0 9px}
.select{height:20px;background:var(--field);margin:0 9px;position:relative}
.select::after{content:"";position:absolute;right:8px;top:7px;border:4px solid transparent;border-top-color:#888}
.area{height:40px;background:var(--field);margin:0 9px}
.check{width:11px;height:11px;background:var(--blue);display:inline-flex;align-items:center;justify-content:center}
.row-inline{display:flex;align-items:center;justify-content:space-between;padding:8px 9px;font-size:9px}

/* dimensions */
.dim-group{padding:6px 9px 0}
.dim-title{display:flex;justify-content:space-between;align-items:center;font-weight:500;font-size:9px;margin-bottom:4px}
.dim-title span{display:flex;gap:5px;align-items:center}
.dim-item{display:flex;justify-content:space-between;align-items:center;font-size:8px;color:var(--muted);padding:3px 0 3px 6px;border-bottom:1px solid var(--line)}
.dim-add{display:flex;margin-top:5px}
.dim-add .field{flex:1;margin:0;height:16px}
.dim-add .add{width:28px;height:16px;background:var(--blue);color:var(--white);font-size:7px;display:flex;align-items:center;justify-content:center}
.x{color:var(--red);font-size:10px;font-weight:700}

/* receipts */
.thumbs{display:flex;gap:7px;padding:10px 9px}
.thumb{width:64px;height:78px;background:linear-gradient(#e9e2d3,#c9b99c);border:3px solid var(--white);box-shadow:0 0 0 1px var(--line)}

/* camera */
.camera{background:#5a5a5a}
.viewfinder{margin:14px 18px 0;flex:1;border:5px solid var(--red);background:#4a4a4a;display:flex;align-items:center;justify-content:center;text-align:center;color:#bdbdbd;font-size:9px;line-height:1.4}
.cam-bar{height:54px;display:flex;align-items:center;justify-content:space-between;padding:0 14px;color:var(--white);font-size:9px;margin-top:14px;background:#6c6c6c}
.shutter{width:30px;height:30px;border-radius:50%;background:var(--red);box-shadow:0 0 0 3px var(--white)}

/* help */
.list-head{background:var(--field);padding:5px 9px;font-size:8px;font-weight:500}
.list-row{display:flex;justify-content:space-between;align-items:center;padding:6px 9px;font-size:8px;border-bottom:1px solid var(--line);background:var(--white)}
.list-row .val{color:var(--muted)}
.list-row.accent{color:var(--red)}
.chev{width:10px;height:10px;border-radius:50%;background:var(--red)}
.article{padding:8px 9px;font-size:7.5px;line-height:1.45;color:#666}

/* splash */
.splash{background:linear-gradient(160deg,#ea5546,#d23f31);align-items:center;justify-content:center}
.splash-logo{display:flex;flex-direction:column;align-items:center;gap:8px;color:var(--white)}
.splash-logo .sq{width:34px;height:34px;border:3px solid var(--white);border-radius:3px}
.splash-logo .nm{font-weight:700;font-size:30px}
.splash-logo .tag{font-size:6px;letter-spacing:1px}
</style>
</head>
<body>

<header class="masthead">
  <div class="brand"><span class="brand-mark"></span>SLIPT</div>
  <div class="masthead-title">PRESENTATION APPS</div>
</header>

<section class="hero">
  <div class="hero-shot home" role="img" aria-label="Photo of a phone on a desk showing the home screen with the SLIPT app icon"></div>
  <div class="hero-shot hand" role="img" aria-label="Photo of a hand holding a phone showing the red SLIPT splash screen">
    <div class="hero-callout">SPLASH<br>SCREEN</div>
  </div>
</section>

<main class="board">

  <!-- Row 1 -->
  <div class="cell">
    <div class="screen splash" role="img" aria-label="Red splash screen with faint receipt photo background">
      <div class="splash-logo"><span class="sq"></span><span class="nm">SLIPT</span><span class="tag">SCAN YOUR RECEIPTS</span></div>
    </div>
    <div class="caption">Splash</div>
  </div>

  <div class="cell">
    <div class="screen">
      <div class="status"></div>
      <div class="nav">
        <div class="nav-side"><svg width="12" height="12"><circle cx="6" cy="6" r="5" fill="none" stroke="#fff" stroke-width="1.5"/></svg></div>
        <span class="nav-name">SLIPT</span>
        <div class="nav-icons"><svg width="11" height="10"><path d="M0 1h11M0 5h11M0 9h11" stroke="#fff" stroke-width="1.6"/></svg><svg width="11" height="11"><circle cx="5.5" cy="5.5" r="4" fill="none" stroke="#fff" stroke-width="2.2" stroke-dasharray="2 1.2"/></svg></div>
      </div>
      <div class="body">
        <div class="scan-button">START<br>SCANNING</div>
        <div class="scan-state">READY</div>
        <div class="counters">
          <div class="counter pending"><span class="name">Pending</span><span class="num">12</span></div>
          <div class="counter sent"><span class="name">Sent</span><span class="num">3</span></div>
        </div>
      </div>
    </div>
    <div class="caption">Main Screen</div>
  </div>

  <div class="cell">
    <div class="screen">
      <div class="status"></div>
      <div class="nav">
        <div class="nav-side"><svg width="12" height="12"><circle cx="6" cy="6" r="5" fill="none" stroke="#fff" stroke-width="1.5"/></svg></div>
        <span class="nav-name">SLIPT</span>
        <div class="nav-icons"><svg width="11" height="10"><path d="M0 1h11M0 5h11M0 9h11" stroke="#fff" stroke-width="1.6"/></svg><svg width="11" height="11"><circle cx="5.5" cy="5.5" r="4" fill="none" stroke="#fff" stroke-width="2.2" stroke-dasharray="2 1.2"/></svg></div>
      </div>
      <div class="body">
        <div class="notice"><span class="ring"></span>Your <strong class="hl">14-Days Trial</strong> period<br>has expired.<br><br><strong>Please <span class="hl">subscribe</span> for the app<br>if you would like to using it</strong></div>
        <div class="stack" style="margin-top:14px"><div class="btn red">Subscribe</div></div>
        <div class="ghost">
          <div class="counter pending"><span class="name">Pending</span><span class="num">12</span></div>
          <div class="counter sent"><span class="name">Sent</span><span class="num">3</span></div>
        </div>
      </div>
    </div>
    <div class="caption">Main Trial Exp</div>
  </div>

  <div class="cell">
    <div class="screen">
      <div class="status"></div>
      <div class="nav">
        <div class="nav-side"><svg width="12" height="12"><circle cx="6" cy="6" r="5" fill="none" stroke="#fff" stroke-width="1.5"/></svg></div>
        <span class="nav-name">SLIPT</span>
        <div class="nav-icons"><svg width="11" height="10"><path d="M0 1h11M0 5h11M0 9h11" stroke="#fff" stroke-width="1.6"/></svg><svg width="11" height="11"><circle cx="5.5" cy="5.5" r="4" fill="none" stroke="#fff" stroke-width="2.2" stroke-dasharray="2 1.2"/></svg></div>
      </div>
      <div class="body">
        <div class="notice" style="margin-top:26px"><span class="ring"></span><strong class="hl">Confirm your subscription</strong><br><br>Do you want to subscribe your<br><strong>SLIPT | 1 Year | for $5</strong><br><br>This subscription will automatically<br>renew until canceled.</div>
        <div class="stack" style="margin-top:16px"><div class="btn blue">Confirm</div><div class="btn red">Cancel</div></div>
        <div class="ghost">
          <div class="counter pending"><span class="name">Pending</span><span class="num">12</span></div>
          <div class="counter sent"><span class="name">Sent</span><span class="num">3</span></div>
        </div>
      </div>
    </div>
    <div class="caption">Main Confirm Sub</div>
  </div>

  <!-- Row 2 -->
  <div class="cell">
    <div class="screen">
      <div class="status"></div>
      <div class="nav">
        <div class="nav-side"><svg width="12" height="12"><circle cx="6" cy="6" r="5" fill="none" stroke="#fff" stroke-width="1.5"/></svg></div>
        <span class="nav-name">SLIPT</span>
        <div class="nav-icons"><svg width="11" height="10"><path d="M0 1h11M0 5h11M0 9h11" stroke="#fff" stroke-width="1.6"/></svg><svg width="11" height="11"><circle cx="5.5" cy="5.5" r="4" fill="none" stroke="#fff" stroke-width="2.2" stroke-dasharray="2 1.2"/></svg></div>
      </div>
      <div class="body">
        <div class="notice" style="margin-top:30px"><span class="ring"></span><strong class="hl">Thank you for subscribing</strong><br>Your purchase was successful<br>to go the Appvault and Review<br>subscription settings or cancel<br>auto-renewal. Tap Manage</div>
        <div class="stack" style="margin-top:18px"><div class="btn blue">OK</div><div class="btn red">Manage</div></div>
        <div class="ghost">
          <div class="counter pending"><span class="name">Pending</span><span class="num">12</span></div>
          <div class="counter sent"><span class="name">Sent</span><span class="num">3</span></div>
        </div>
      </div>
    </div>
    <div class="caption">Main Thank you</div>
  </div>

  <div class="cell">
    <div class="screen">
      <div class="status"></div>
      <div class="nav">
        <div class="nav-side"><svg width="9" height="14"><path d="M7 1 2 7l5 6" fill="none" stroke="#fff" stroke-width="2"/></svg></div>
        <span class="nav-name">SLIPT</span>
        <div class="nav-icons"></div>
      </div>
      <div class="section-head">☰ Dimensions</div>
      <div class="body">
        <div class="dim-group">
          <div class="dim-title">Daily cost <span>Active <i class="check"><svg width="8" height="7"><path d="M1 3.5 3 6l4-5" fill="none" stroke="#fff" stroke-width="1.5"/></svg></i></span></div>
          <div class="dim-item">Drink <span class="x">✕</span></div>
          <div class="dim-item">Snack <span class="x">✕</span></div>
          <div class="dim-item">Transport <span class="x">✕</span></div>
          <div class="dim-add"><div class="field"></div><div class="add">Add</div></div>
        </div>
        <div class="dim-group" style="padding-top:10px">
          <div class="dim-title">Bill <span>Active <i class="check" style="background:var(--line)"></i></span></div>
          <div class="dim-item">Credit Card <span class="x">✕</span></div>
          <div class="dim-add"><div class="field"></div><div class="add">Add</div></div>
        </div>
        <div class="stack"><div class="btn teal">Save</div><div class="btn blue">Close</div></div>
      </div>
    </div>
    <div class="caption">Dimension</div>
  </div>

  <div class="cell">
    <div class="screen">
      <div class="status"></div>
      <div class="nav">
        <div class="nav-side"><svg width="9" height="14"><path d="M7 1 2 7l5 6" fill="none" stroke="#fff" stroke-width="2"/></svg></div>
        <span class="nav-name">SLIPT</span>
        <div class="nav-icons"></div>
      </div>
      <div class="section-head">⚙ Settings</div>
      <div class="body">
        <div class="field-label">Email</div><div class="field"></div>
        <div class="field-label">CC</div><div class="field"></div>
        <div class="field-label">Name</div><div class="field"></div>
        <div class="row-inline">Save to Camera Roll <i class="check"><svg width="8" height="7"><path d="M1 3.5 3 6l4-5" fill="none" stroke="#fff" stroke-width="1.5"/></svg></i></div>
        <div class="stack"><div class="btn teal">Save</div><div class="btn blue">Close</div></div>
      </div>
    </div>
    <div class="caption">Settings</div>
  </div>

  <div class="cell">
    <div class="screen">
      <div class="status"></div>
      <div class="nav">
        <div class="nav-side"><svg width="9" height="14"><path d="M7 1 2 7l5 6" fill="none" stroke="#fff" stroke-width="2"/></svg></div>
        <span class="nav-name">SLIPT</span>
        <div class="nav-icons"></div>
      </div>
      <div class="section-head">▤ Pending Receipts</div>
      <div class="body">
        <div class="thumbs">
          <div class="thumb" role="img" aria-label="Receipt photo"></div>
          <div class="thumb" role="img" aria-label="Receipt photo"></div>
          <div class="thumb" role="img" aria-label="Receipt photo"></div>
        </div>
        <div class="thumbs" style="padding-top:0"><div class="thumb" role="img" aria-label="Receipt photo"></div></div>
        <div class="stack"><div class="btn teal">Send All</div><div class="btn red">Delete All</div><div class="btn blue">Close</div></div>
      </div>
    </div>
    <div class="caption">Pending</div>
  </div>

  <!-- Row 3 -->
  <div class="cell">
    <div class="screen">
      <div class="status"></div>
      <div class="nav">
        <div class="nav-side"><svg width="9" height="14"><path d="M7 1 2 7l5 6" fill="none" stroke="#fff" stroke-width="2"/></svg></div>
        <span class="nav-name">SLIPT</span>
        <div class="nav-icons"></div>
      </div>
      <div class="section-head">▤ Sent Receipts</div>
      <div class="body">
        <div class="thumbs">
          <div class="thumb" role="img" aria-label="Receipt photo"></div>
          <div class="thumb" role="img" aria-label="Receipt photo"></div>
          <div class="thumb" role="img" aria-label="Receipt photo"></div>
        </div>
        <div class="stack"><div class="btn red">Delete All</div><div class="btn blue">Close</div></div>
      </div>
    </div>
    <div class="caption">Sent</div>
  </div>

  <div class="cell">
    <div class="screen camera">
      <div class="status"></div>
      <div class="nav">
        <div class="nav-side"><svg width="9" height="14"><path d="M7 1 2 7l5 6" fill="none" stroke="#fff" stroke-width="2"/></svg></div>
        <span class="nav-name">SLIPT</span>
        <div class="nav-icons"></div>
      </div>
      <div class="viewfinder">RECEIPT<br>IMAGE<br>TO SCAN</div>
      <div class="cam-bar"><span>Cancel</span><span class="shutter"></span><span>From Photos</span></div>
    </div>
    <div class="caption">Scan</div>
  </div>

  <div class="cell">
    <div class="screen camera">
      <div class="status"></div>
      <div class="nav">
        <div class="nav-side"><svg width="9" height="14"><path d="M7 1 2 7l5 6" fill="none" stroke="#fff" stroke-width="2"/></svg></div>
        <span class="nav-name">SLIPT</span>
        <div class="nav-icons"></div>
      </div>
      <div class="viewfinder">Preview<br>Scan</div>
      <div class="cam-bar"><span>Retake</span><span>Continue</span></div>
    </div>
    <div class="caption">Scan Preview</div>
  </div>

  <div class="cell">
    <div class="screen">
      <div class="status"></div>
      <div class="nav">
        <div class="nav-side"><svg width="9" height="14"><path d="M7 1 2 7l5 6" fill="none" stroke="#fff" stroke-width="2"/></svg></div>
        <span class="nav-name">SLIPT</span>
        <div class="nav-icons"></div>
      </div>
      <div class="section-head">⚙ Settings</div>
      <div class="body">
        <div class="field-label">Type of cost</div><div class="select"></div>
        <div class="field-label">Payment Method</div><div class="select"></div>
        <div class="field-label">Dimension</div><div class="select"></div>
        <div class="field-label">Description</div><div class="area"></div>
        <div class="stack"><div class="btn teal">Send</div><div class="btn blue">Cancel</div></div>
      </div>
    </div>
    <div class="caption">Scan Upload</div>
  </div>

  <!-- Row 4 -->
  <div class="cell">
    <div class="screen">
      <div class="status"></div>
      <div class="nav">
        <div class="nav-side"><svg width="12" height="12"><circle cx="6" cy="6" r="5" fill="none" stroke="#fff" stroke-width="1.5"/></svg></div>
        <span class="nav-name">SLIPT</span>
        <div class="nav-icons"><svg width="11" height="10"><path d="M0 1h11M0 5h11M0 9h11" stroke="#fff" stroke-width="1.6"/></svg><svg width="11" height="11"><circle cx="5.5" cy="5.5" r="4" fill="none" stroke="#fff" stroke-width="2.2" stroke-dasharray="2 1.2"/></svg></div>
      </div>
      <div class="body">
        <div class="scan-button">START<br>SCANNING</div>
        <div class="scan-state">UPLOADED</div>
        <div class="counters">
          <div class="counter pending"><span class="name">Pending</span><span class="num">12</span></div>
          <div class="counter sent"><span class="name">Sent</span><span class="num">3</span></div>
        </div>
      </div>
    </div>
    <div class="caption">Upload Complete</div>
  </div>

  <div class="cell">
    <div class="screen">
      <div class="status"></div>
      <div class="nav">
        <div class="nav-side"><svg width="9" height="14"><path d="M7 1 2 7l5 6" fill="none" stroke="#fff" stroke-width="2"/></svg></div>
        <span class="nav-name">SLIPT</span>
        <div class="nav-icons"></div>
      </div>
      <div class="section-head">❓ Help</div>
      <div class="body">
        <div class="list-head">Account</div>
        <div class="list-row">Email <span class="val">user@mail.com</span></div>
        <div class="list-row">Subscription <span class="val">Trial</span></div>
        <div class="list-row accent">Upgrade Now <span class="chev"></span></div>
        <div class="list-head">More</div>
        <div class="list-row">About <span class="chev"></span></div>
        <div class="list-row">Privacy Policy <span class="chev"></span></div>
        <div class="list-row">Support <span class="chev"></span></div>
        <div class="list-row">Feedback <span class="chev"></span></div>
      </div>
    </div>
    <div class="caption">Help</div>
  </div>

  <div class="cell">
    <div class="screen">
      <div class="status"></div>
      <div class="nav">
        <div class="nav-side"><svg width="9" height="14"><path d="M7 1 2 7l5 6" fill="none" stroke="#fff" stroke-width="2"/></svg></div>
        <span class="nav-name">SLIPT</span>
        <div class="nav-icons"></div>
      </div>
      <div class="section-head">❓ Help</div>
      <div class="body">
        <div class="list-head">Account</div>
        <div class="list-row">Email <span class="val">user@mail.com</span></div>
        <div class="list-row">Subscription <span class="val">1 Year</span></div>
        <div class="list-row">Manage Your Subscription <span class="chev"></span></div>
        <div class="list-head">More</div>
        <div class="list-row">About <span class="chev"></span></div>
        <div class="list-row">Privacy Policy <span class="chev"></span></div>
        <div class="list-row">Support <span class="chev"></span></div>
        <div class="list-row">Feedback <span class="chev"></span></div>
      </div>
    </div>
    <div class="caption">Help Subscription</div>
  </div>

  <div class="cell">
    <div class="screen">
      <div class="status"></div>
      <div class="nav">
        <div class="nav-side"><svg width="9" height="14"><path d="M7 1 2 7l5 6" fill="none" stroke="#fff" stroke-width="2"/></svg></div>
        <span class="nav-name">SLIPT</span>
        <div class="nav-icons"></div>
      </div>
      <div class="section-head">❓ Help</div>
      <div class="body">
        <p class="article">Lorem ipsum dolor sit amet, consectetur adipiscing elit, sed diam nonummy nibh euismod tincidunt ut laoreet dolore magna aliquam erat volutpat. Ut wisi enim ad minim veniam, quis nostrud exerci tation ullamcorper suscipit lobortis nisl ut aliquip ex ea commodo consequat. Duis autem vel eum iriure dolor in hendrerit in vulputate velit esse molestie consequat, vel illum dolore eu feugiat nulla facilisis at vero eros et accumsan et iusto odio dignissim qui blandit praesent luptatum zzril delenit augue duis dolore te feugait nulla facilisi.</p>
        <div class="stack"><div class="btn blue">Close</div></div>
      </div>
    </div>
    <div class="caption">Help Article</div>
  </div>

</main>
</body>
</html>
```